Hydrographic business needs a business card that reaches hunters and off-road enthusiasts

We need a business card for a new hydrographics company catering to customers such as hunters, off-road ATV riders and custom vehicle enthusiasts. A western theme is preferred but professional. Our service should be thought of as upper end graphic design on firearms, off road vehicles, motorcycles, etc... See www.caldorfx.com for ideas on patterns, colors, etc...

Target Market(s)

Hunters, off road enthusiasts, custom car enthusiasts, motorcycle riders...

Industry/Entity Type

Graphic Design

```html
<!DOCTYPE html>
<html lang="en">
<head>
<meta charset="utf-8">
<title>Caldor Hydro Graphics – Business Card</title>
<link href="https://fonts.googleapis.com/css2?family=Arvo:wght@400;700&family=Roboto+Condensed:wght@400&family=Roboto:wght@400&display=swap" rel="stylesheet">
<style>
  :root {
    --page: #f2f2f2;
    --card: #b8a887;
    --brown: #4a2508;
    --white: #ffffff;
  }
  * { box-sizing: border-box; margin: 0; padding: 0; }
  html, body { width: 1200px; height: 900px; overflow: hidden; }
  body { background: var(--page); position: relative; font-family: "Arvo", serif; color: var(--brown); }

  .card {
    position: absolute;
    width: 638px;
    height: 355px;
    background: var(--card);
    overflow: hidden;
  }
  .card-front { left: 125px; top: 108px; }
  .card-back  { left: 390px; top: 443px; }

  .edge { position: absolute; top: 0; bottom: 0; background: var(--brown); }
  .edge-left  { left: 0; width: 30px; }
  .edge-right { right: 0; width: 22px; }

  .rule { position: absolute; height: 2px; background: var(--brown); }

  /* Front */
  .brand-front {
    position: absolute; left: 0; right: 0; top: 92px;
    text-align: center;
  }
  .brand-dot {
    display: block; width: 40px; height: 40px; border-radius: 50%;
    background: var(--brown); margin: 0 auto 18px;
  }
  .brand-name {
    font-family: "Arvo", serif; font-weight: 700; font-size: 30px;
    letter-spacing: 1px; line-height: 1.15; text-transform: uppercase;
  }
  .services {
    position: absolute; left: 0; right: 0; top: 276px;
    text-align: center; font-weight: 700; font-size: 23px; white-space: nowrap;
  }

  /* Back */
  .brand-back {
    position: absolute; left: 44px; top: 34px; width: 110px;
    text-align: center;
  }
  .brand-back .brand-dot { width: 22px; height: 22px; margin-bottom: 8px; }
  .brand-back .brand-name { font-size: 14px; letter-spacing: 0.5px; }

  .wanted {
    position: absolute; left: 160px; top: 24px;
    font-weight: 700; font-size: 62px; letter-spacing: 1px; line-height: 1;
    white-space: nowrap;
  }
  .contact { position: absolute; left: 156px; top: 108px; }
  .person { font-weight: 700; font-size: 34px; line-height: 1.1; white-space: nowrap; }
  .phone  { font-weight: 700; font-size: 50px; line-height: 1.1; white-space: nowrap; }
  .address {
    font-family: "Roboto Condensed", sans-serif; font-size: 14px; margin-top: 8px; white-space: nowrap;
  }
  .email {
    font-family: "Roboto Condensed", sans-serif; font-size: 17px; margin-top: 6px;
  }
  .website {
    display: inline-block; margin-top: 12px;
    background: var(--brown); color: var(--white);
    font-family: "Roboto", sans-serif; font-size: 28px; line-height: 1;
    padding: 4px 10px 5px 8px;
  }
  .tagline {
    position: absolute; left: 60px; top: 305px;
    font-weight: 700; font-size: 17px; white-space: nowrap;
  }
</style>
</head>
<body>

  <section class="card card-front" aria-label="Card front">
    <div class="edge edge-left"></div>
    <div class="edge edge-right"></div>
    <div class="brand-front">
      <span class="brand-dot"></span>
      <div class="brand-name">Caldor<br>Hydro Graphics</div>
    </div>
    <div class="services">Firearms &nbsp;·&nbsp; ATVs &nbsp;·&nbsp; Side by side</div>
    <div class="rule" style="left:125px; width:400px; top:308px;"></div>
  </section>

  <section class="card card-back" aria-label="Card back">
    <div class="edge edge-left"></div>
    <div class="edge edge-right"></div>
    <div class="brand-back">
      <span class="brand-dot"></span>
      <div class="brand-name">Caldor Hydro Graphics</div>
    </div>
    <div class="rule" style="left:150px; width:340px; top:20px;"></div>
    <h1 class="wanted">WANTED</h1>
    <div class="rule" style="left:150px; width:340px; top:95px;"></div>
    <div class="contact">
      <div class="person">Wade Caldor</div>
      <div class="phone">214-555-0187</div>
      <div class="address">612 Mesa County Road 2140 Red Fork, TX 75000</div>
      <div class="email">wade@caldorfx.com</div>
      <div class="website">www.caldorfx.com</div>
    </div>
    <div class="rule" style="left:45px; width:550px; top:302px;"></div>
    <div class="tagline">The best and most reliable hydrographics service in Texas</div>
    <div class="rule" style="left:55px; width:540px; top:330px;"></div>
  </section>

</body>
</html>
```